New Web Site - Professional Cleaning Company

I want to create a new attractive website that acts as an advertisement to visitors to entice them to reach out for more information.
We are a commercial/business janitorial service - with a new logo, would like the font to be complimentary to the font of logo, as well as the color scheme.
Target Market(s)
Commercial buildings, schools & medical buildings
Industry/Entity Type
Janitorial
Coding
Coded - Design and coding required
Number of Pages Required
4 page
Requirements
Must have
- Professionalism, sharp imagery

```html
<!DOCTYPE html>
<html lang="en">
<head>
<meta charset="utf-8">
<title>Brightwell Facility Services — Professional Cleaning</title>
<link href="https://fonts.googleapis.com/css2?family=Orbitron:wght@600;700;800;900&family=Poppins:wght@400;500;600;700&display=swap" rel="stylesheet">
<style>
:root{
  --navy:#1b2a6b;
  --navy-deep:#14215a;
  --blue:#1b8ad0;
  --blue-light:#e3f1f8;
  --green:#3aa935;
  --green-dark:#2e8f2a;
  --ink:#141414;
  --text:#555a66;
  --white:#ffffff;
}
*{box-sizing:border-box;margin:0;padding:0}
html,body{width:1200px;height:3781px;overflow:hidden}
body{position:relative;background:var(--white);font-family:"Poppins",sans-serif;color:var(--text)}
.abs{position:absolute}
.display{font-family:"Orbitron",sans-serif;text-transform:uppercase;font-weight:700;letter-spacing:0}

/* header */
.topbar{top:0;left:0;width:1200px;height:40px}
.call{top:8px;left:707px;color:var(--white);font-weight:600;font-size:17px;display:flex;align-items:center;gap:8px}
.call-icon{width:24px;height:24px;border:2px solid var(--white);border-radius:50%;display:flex;align-items:center;justify-content:center}
.nav a{position:absolute;top:80px;font-weight:600;font-size:15px;color:var(--ink);text-decoration:none}
.nav .active-ring{position:absolute;top:71px;left:145px;width:36px;height:36px;border:2px solid var(--blue);border-radius:50%;border-right-color:transparent}
.brand{top:15px;left:527px;width:146px;height:146px;border-radius:50%;background:var(--white);border:3px solid var(--blue);display:flex;align-items:center;justify-content:center;text-align:center;z-index:5}
.brand span{font-weight:700;font-size:14px;line-height:1.3;color:var(--navy)}

.btn{display:flex;align-items:center;justify-content:space-between;background:var(--green);color:var(--white);border-radius:30px;font-weight:600;font-size:13px;text-transform:uppercase;padding-left:26px;text-decoration:none}
.btn .dot{width:40px;height:40px;border-radius:50%;background:var(--white);border:3px solid var(--green);display:flex;align-items:center;justify-content:center;margin-right:1px}

/* hero */
.hero{top:129px;left:0;width:1200px;height:700px}
.hero-text{top:540px;left:323px;width:557px;text-align:center;color:var(--white)}
.hero-text .kicker{font-weight:600;font-size:19px}
.hero-text h1{font-size:40px;line-height:50px;margin-top:20px}
.dots span{position:absolute;left:1138px;width:8px;height:8px;border-radius:50%;background:var(--white)}
.dots span.on{background:var(--green)}

/* section heads */
.ghost{font-family:"Orbitron",sans-serif;font-weight:900;font-size:100px;color:#eef0f3;line-height:1;white-space:nowrap}
.head{left:0;width:1200px;text-align:center}
.head .l1{font-size:38px;color:var(--ink);font-weight:800}
.head .l2{font-size:28px;color:var(--navy);margin-top:10px;font-weight:600}
.rule{width:50px;height:3px;background:var(--green);margin:20px auto 0}

.welcome-bg{top:1010px;left:0;width:1200px;height:650px;background:linear-gradient(180deg,rgba(255,255,255,1) 0%,rgba(226,232,240,.8) 35%,rgba(205,214,226,.8) 100%)}
.intro{top:1052px;left:170px;width:860px;text-align:center;font-size:15.5px;line-height:31px;color:#3b3f48}

/* targets */
.card{color:var(--white);text-align:center}
.card h3{font-weight:700;font-size:17px;line-height:26px;margin-top:14px;text-transform:uppercase}
.card p{font-size:10.5px;line-height:20px;margin-top:10px}
.card .more{display:inline-block;font-weight:700;font-size:13px;margin-top:16px;border-bottom:1px solid var(--white);text-transform:uppercase}
.card-green{top:1709px;left:139px;width:300px;height:360px;background:linear-gradient(160deg,#2f9a35,#1c6b25);clip-path:polygon(0 30px,100% 0,100% 100%,0 100%);padding:40px 40px 0}
.card-blue{top:1709px;left:762px;width:297px;height:360px;background:linear-gradient(200deg,#1e8fd6,#0f5f9e);clip-path:polygon(0 0,100% 30px,100% 100%,0 100%);padding:40px 40px 0}
.card-navy{top:1652px;left:434px;width:331px;height:418px;border-radius:22px 22px 0 0;background:linear-gradient(180deg,#1d2f7d,#0d184a);padding:36px 44px 0;box-shadow:0 10px 30px rgba(0,0,0,.25);z-index:2}

/* blog */
.blog-grid{top:2462px;left:142px;width:914px;height:490px;display:grid;grid-template-columns:repeat(3,1fr);grid-template-rows:repeat(2,1fr);border:1px solid #e3e5ea;background:var(--white)}
.post{text-align:center;padding:34px 28px 0}
.post h4{font-weight:700;font-size:15.5px;color:var(--ink);text-transform:uppercase}
.post .date{font-size:12.5px;color:var(--blue);margin-top:10px;display:flex;align-items:center;justify-content:center;gap:5px}
.post p{font-size:12.5px;line-height:22px;color:#6a6e78;margin-top:14px}
.post .more{display:inline-block;margin-top:18px;font-weight:700;font-size:13.5px;color:var(--green);border-bottom:1px solid var(--green);text-transform:uppercase}
.photo{width:100%;height:100%}

/* contact */
.contact-bg{top:3090px;left:0;width:1200px;height:691px}
.contact-title{top:3278px;left:0;width:1200px;text-align:center;color:var(--white);font-size:40px}
.label{font-weight:600;font-size:15px;color:var(--white);text-transform:uppercase}
.field{background:var(--white);border:none;font-family:"Poppins",sans-serif;font-size:10px;color:#555;padding:8px 12px;display:block}
.submit{top:3615px;left:609px;width:78px;height:27px;border-radius:14px;background:var(--green);color:var(--white);font-weight:600;font-size:11px;display:flex;align-items:center;justify-content:center;text-transform:uppercase}
.info{left:757px;display:flex;align-items:center;gap:16px;color:var(--white);font-size:12.5px;line-height:17px}
.info .ic{width:34px;height:34px;border-radius:50%;border:2px solid var(--white);display:flex;align-items:center;justify-content:center;flex:none}
.footer-line{top:3693px;left:132px;width:936px;height:1px;background:rgba(255,255,255,.25)}
.copy{top:3725px;left:142px;font-size:12.5px;color:var(--white)}
.social{top:3721px;left:892px;display:flex;gap:10px}
.social span{width:26px;height:26px;border-radius:50%;display:block}
</style>
</head>
<body>

<!-- header -->
<svg class="abs topbar" viewBox="0 0 1200 40" aria-hidden="true">
  <path d="M640,0 L1200,0 L1200,36 L700,36 Q662,36 640,0 Z" fill="var(--blue)"/>
</svg>
<div class="abs call"><span class="call-icon"><svg width="12" height="12" viewBox="0 0 24 24"><path d="M6.6 10.8a15 15 0 0 0 6.6 6.6l2.2-2.2a1 1 0 0 1 1-.25 11.4 11.4 0 0 0 3.6.57 1 1 0 0 1 1 1V20a1 1 0 0 1-1 1A17 17 0 0 1 3 4a1 1 0 0 1 1-1h3.5a1 1 0 0 1 1 1c0 1.25.2 2.45.57 3.57a1 1 0 0 1-.25 1z" fill="#fff"/></svg></span>CALL : +1 555 010 2040</div>

<nav class="nav">
  <span class="active-ring"></span>
  <a style="left:164px">HOME</a>
  <a style="left:246px">ABOUT</a>
  <a style="left:336px">SERVICES</a>
  <a style="left:447px">NEWS</a>
  <a style="left:713px">CONTACT</a>
</nav>
<div class="abs brand"><span>BRIGHTWELL<br>FACILITY<br>SERVICES</span></div>
<a class="abs btn" style="top:69px;left:817px;width:239px;height:42px;font-size:12px;padding-left:20px">Request an appointment<span class="dot"><svg width="14" height="14" viewBox="0 0 24 24"><path d="M5 12h13M13 6l6 6-6 6" stroke="var(--green)" stroke-width="3" fill="none"/></svg></span></a>

<!-- hero -->
<svg class="abs hero" viewBox="0 0 1200 700">
  <defs>
    <linearGradient id="sky" x1="0" y1="0" x2="1" y2="1">
      <stop offset="0" stop-color="#6fa8de"/><stop offset=".5" stop-color="#2f63ab"/><stop offset="1" stop-color="#163b7c"/>
    </linearGradient>
  </defs>
  <rect width="1200" height="700" fill="url(#sky)" role="img" aria-label="Photo of glass office towers against a cloudy blue sky"/>
  <path d="M323,700 L323,470 Q323,311 601,311 Q880,311 880,470 L880,700 Z" fill="var(--navy)"/>
  <path d="M0,370 Q600,900 1200,370 L1200,700 L0,700 Z" fill="var(--blue)"/>
  <path d="M0,410 Q600,940 1200,400 L1200,700 L0,700 Z" fill="var(--white)"/>
  <rect x="770" y="548" width="58" height="82" rx="12" fill="#4db84a" opacity=".85" role="img" aria-label="Illustration of a cleaner holding a broom"/>
</svg>
<div class="dots"><span style="top:356px"></span><span class="on" style="top:375px"></span><span style="top:394px"></span><span style="top:413px"></span></div>
<div class="abs hero-text">
  <div class="kicker">WELCOME TO</div>
  <h1 class="display">Professional<br>Cleaning</h1>
</div>
<a class="abs btn" style="top:705px;left:472px;width:255px;height:44px;font-size:12px;padding-left:22px">Request an appointment<span class="dot"><svg width="14" height="14" viewBox="0 0 24 24"><path d="M5 12h13M13 6l6 6-6 6" stroke="var(--green)" stroke-width="3" fill="none"/></svg></span></a>

<!-- welcome -->
<div class="abs welcome-bg" role="img" aria-label="Faded photo of laboratory staff in white coats"></div>
<div class="abs ghost" style="top:862px;left:0">WELCOME</div>
<div class="abs head" style="top:897px">
  <div class="l1 display">Welcome to</div>
  <div class="l2 display">Brightwell Facility Services</div>
  <div class="rule"></div>
</div>
<p class="abs intro">Lorem ipsum dolor sit amonsectetur adipiscing elied do eiusmod tempor incididunt ut labore et dolores ipsum suspendisse ultrices cenas accumsan lacus vel facilisis. Lorem ipsum dolor sit amonsectetur adipiscing elied do eiusmod tempor incididunt ut labore et dolores ipsum suspendisse ultrices cenas accumsan lacus vel facilisis. Lorem ipsum dolor sit amonsectetur adipiscing elied do eiusmod tempor incididunt ut labore et dolores ipsumsuspendisse ultrices cenas accumsan lacus vel facilisis.</p>
<a class="abs btn" style="top:1242px;left:509px;width:181px;height:46px">Read more<span class="dot"><svg width="14" height="14" viewBox="0 0 24 24"><path d="M5 12h13M13 6l6 6-6 6" stroke="var(--green)" stroke-width="3" fill="none"/></svg></span></a>

<!-- targets -->
<svg class="abs" style="top:1370px;left:0" width="1200" height="700" viewBox="0 0 1200 700" aria-hidden="true">
  <path d="M0,290 Q600,-260 1200,280 L1200,700 L0,700 Z" fill="var(--blue)"/>
  <path d="M0,306 Q600,-236 1200,296 L1200,700 L0,700 Z" fill="var(--blue-light)"/>
</svg>
<div class="abs ghost" style="top:1612px;left:820px;color:rgba(255,255,255,.7)">TARGETS</div>
<div class="abs head" style="top:1490px">
  <div class="l1 display">Our</div>
  <div class="l2 display">Targets are</div>
  <div class="rule"></div>
</div>

<div class="abs card card-green">
  <svg width="80" height="84" viewBox="0 0 80 84" fill="none" stroke="#fff" stroke-width="3"><rect x="6" y="30" width="26" height="52"/><rect x="32" y="8" width="24" height="74"/><rect x="56" y="40" width="18" height="42"/><path d="M12 40h14M12 52h14M12 64h14M38 20h12M38 32h12M38 44h12M38 56h12M62 52h6M62 64h6"/></svg>
  <h3>Commercial<br>Buildings</h3>
  <p>Lorem ipsum dolor sit amet, consectetur adipiscing elit, sed do eiusmod tempor incididunt ut labore et dolore</p>
  <span class="more">Read more</span>
</div>
<div class="abs card card-navy">
  <svg width="104" height="100" viewBox="0 0 104 100" fill="none" stroke="#fff" stroke-width="3"><path d="M52 4v14M52 4h14v8H52"/><path d="M30 40l22-22 22 22"/><rect x="30" y="40" width="44" height="56"/><circle cx="52" cy="54" r="8"/><rect x="4" y="50" width="26" height="46"/><rect x="74" y="50" width="26" height="46"/><path d="M44 96V76h16v20M10 62h14M10 78h14M80 62h14M80 78h14"/></svg>
  <h3 style="margin-top:18px">Schools</h3>
  <p style="line-height:21px">Lorem ipsum dolor sit amet, consectetur adipiscing elit, sed do eiusmod temididunt ut labore et doloreagna aliquais ipsum suspendisse ultrices gravidaus commodo viverra maecenas accumsan lacus vel fanon numquamcilisis.</p>
  <span class="more">Read more</span>
</div>
<div class="abs card card-blue">
  <svg width="86" height="86" viewBox="0 0 86 86" fill="none" stroke="#fff" stroke-width="3"><rect x="8" y="28" width="70" height="56"/><rect x="26" y="4" width="34" height="30" fill="#1a7cc0"/><path d="M43 10v18M34 19h18M20 44h10M38 44h10M56 44h10M20 58h10M56 58h10M36 84V62h14v22"/></svg>
  <h3>Medical<br>Buildings</h3>
  <p>Lorem ipsum dolor sit amet, consectetur adipiscing elit, sed do eiusmod tempor incididunt ut labore et dolore</p>
  <span class="more">Read more</span>
</div>
<div class="abs" style="top:1994px;left:706px;width:52px;height:74px;border-radius:12px;background:#4db84a;z-index:3" role="img" aria-label="Illustration of a cleaner holding a broom"></div>

<!-- blog -->
<div class="abs ghost" style="top:2290px;left:862px">BLOG</div>
<div class="abs head" style="top:2290px">
  <div class="l1 display">Our</div>
  <div class="l2 display">Latest blogs</div>
  <div class="rule"></div>
</div>
<div class="abs" style="top:2420px;left:0;width:1200px;height:700px;background:linear-gradient(180deg,rgba(230,238,246,0) 0%,rgba(226,236,245,.8) 60%,rgba(226,236,245,.5) 100%)" role="img" aria-label="Faint illustration of buildings and a cleaner"></div>
<div class="abs blog-grid">
  <div class="photo" style="background:linear-gradient(135deg,#b9c8d4,#7c8fa0 50%,#c8b89a)" role="img" aria-label="Photo of a teacher in a classroom"></div>
  <div class="post"><h4>At vero eos eaccusamu</h4><div class="date"><svg width="11" height="11" viewBox="0 0 12 12" fill="none" stroke="currentColor"><rect x="1" y="2" width="10" height="9"/><path d="M1 5h10M4 1v2M8 1v2"/></svg>Jan 07,2022</div><p>At vero eos et accusamus et iusto odio dignissiducimumos ducimus qui blanditiis pducimuducimuraesentiu</p><span class="more">Read more</span></div>
  <div class="photo" style="background:linear-gradient(135deg,#9fb0c0,#6f8194 50%,#b8c4cf)" role="img" aria-label="Photo of a worker mopping an industrial floor"></div>
  <div class="post"><h4>At vero eos eaccusamu</h4><div class="date"><svg width="11" height="11" viewBox="0 0 12 12" fill="none" stroke="currentColor"><rect x="1" y="2" width="10" height="9"/><path d="M1 5h10M4 1v2M8 1v2"/></svg>Jan 07,2022</div><p>At vero eos et accusamus et iusto odio dignissiducimumos ducimus qui blanditiis pducimuducimuraesentiu</p><span class="more">Read more</span></div>
  <div class="photo" style="background:linear-gradient(180deg,#d8e9f3,#7fb4d6 55%,#4f8fbd)" role="img" aria-label="Photo of a clean hospital corridor"></div>
  <div class="post"><h4>At vero eos eaccusamu</h4><div class="date"><svg width="11" height="11" viewBox="0 0 12 12" fill="none" stroke="currentColor"><rect x="1" y="2" width="10" height="9"/><path d="M1 5h10M4 1v2M8 1v2"/></svg>Jan 07,2022</div><p>At vero eos et accusamus et iusto odio dignissiducimumos ducimus qui blanditiis pducimuducimuraesentiu</p><span class="more">Read more</span></div>
</div>
<a class="abs btn" style="top:3003px;left:509px;width:181px;height:46px">View more<span class="dot"><svg width="14" height="14" viewBox="0 0 24 24"><path d="M5 12h13M13 6l6 6-6 6" stroke="var(--green)" stroke-width="3" fill="none"/></svg></span></a>

<!-- contact -->
<svg class="abs contact-bg" viewBox="0 0 1200 691" aria-hidden="true">
  <path d="M0,285 Q600,-250 1200,225 L1200,691 L0,691 Z" fill="var(--blue)"/>
  <path d="M0,305 Q600,-225 1200,245 L1200,691 L0,691 Z" fill="var(--navy)"/>
</svg>
<div class="abs ghost" style="top:3240px;left:310px;color:rgba(255,255,255,.05)">CONTACT</div>
<div class="abs" style="top:3175px;left:975px;width:66px;height:92px;border-radius:12px;background:#4db84a" role="img" aria-label="Illustration of a cleaner holding a broom"></div>
<div class="abs contact-title display">Contact</div>
<div class="abs" style="top:3345px;left:575px;width:50px;height:3px;background:var(--green)"></div>

<div class="abs label" style="top:3405px;left:142px">Get in touch</div>
<div class="abs field" style="top:3449px;left:145px;width:266px;height:29px">NAME :</div>
<div class="abs field" style="top:3449px;left:421px;width:266px;height:29px">PHONE :</div>
<div class="abs field" style="top:3490px;left:145px;width:542px;height:29px">EMAIL :</div>
<div class="abs field" style="top:3531px;left:145px;width:542px;height:64px">MESSAGE :</div>
<div class="abs submit">Submit</div>

<div class="abs label" style="top:3405px;left:757px">Contact information</div>
<div class="abs info" style="top:3450px"><span class="ic"><svg width="14" height="14" viewBox="0 0 24 24"><path d="M12 2a7 7 0 0 0-7 7c0 5 7 13 7 13s7-8 7-13a7 7 0 0 0-7-7zm0 9.5A2.5 2.5 0 1 1 12 6.5a2.5 2.5 0 0 1 0 5z" fill="#fff"/></svg></span><span>233,Sed ut perspiciatinde omnis iste<br>natus error sit voluptatem</span></div>
<div class="abs info" style="top:3497px"><span class="ic" style="background:var(--blue);border-color:var(--blue)"><svg width="14" height="14" viewBox="0 0 24 24"><path d="M6.6 10.8a15 15 0 0 0 6.6 6.6l2.2-2.2a1 1 0 0 1 1-.25 11.4 11.4 0 0 0 3.6.57 1 1 0 0 1 1 1V20a1 1 0 0 1-1 1A17 17 0 0 1 3 4a1 1 0 0 1 1-1h3.5a1 1 0 0 1 1 1c0 1.25.2 2.45.57 3.57a1 1 0 0 1-.25 1z" fill="#fff"/></svg></span><span style="font-weight:600;font-size:14px">Phone : +1 555 010 2040</span></div>
<div class="abs info" style="top:3543px"><span class="ic"><svg width="14" height="14" viewBox="0 0 24 24"><rect x="3" y="5" width="18" height="14" rx="2" fill="#fff"/><path d="M3 7l9 6 9-6" stroke="var(--navy)" stroke-width="2" fill="none"/></svg></span><span>mail@brightwellfs.co<br>billing@brightwellfs.co</span></div>
<div class="abs info" style="top:3590px"><span class="ic"><svg width="14" height="14" viewBox="0 0 24 24" fill="none" stroke="#fff" stroke-width="2.5"><circle cx="12" cy="12" r="9"/><path d="M12 7v5l3 2"/></svg></span><span style="font-weight:600;font-size:16px">24/7</span></div>

<div class="abs footer-line"></div>
<div class="abs copy">Copyrights © 2022, Companyname. All Rights Reserved. &nbsp;|&nbsp; Privacy policy</div>
<div class="abs social" aria-label="Social media links">
  <span style="background:var(--navy);border:1px solid rgba(255,255,255,.4)"></span>
  <span style="background:var(--blue)"></span>
  <span style="background:#c9302c"></span>
  <span style="background:#a8825a"></span>
  <span style="background:var(--blue)"></span>
</div>

</body>
</html>
```